Financial Services Consultant needs a business card

We need a business card for a new consulting company based in Melbourne called
"Korvane Metrics". Tagline is Assess, Adjust, Advance
We would like to see business card designs that are in line with the minimal style of the website www.korvane-metrics-example.com
The font I have used on the website is Proxima Nova and would like the same or similar font used on the business card with a minimal design in line with the website Two sided with "KORVANE METRICS" ASSESS, ADJUST, ADVANCE on one side and name, title and contact details on the otther
Updates

Hi All, thanks for your submissions, much appreciated.

I have recently added some colour to my webiste, it is hex #3a7b74 for those that wish to use it
Thanks

Hi all

thanks very much for your design submissions I am very impressed and they are much appreciated.

Interms of general feedback please find below;

Colour: I am trying to stick to a minimal design and colour scheme for my website which is still under construction, up to 3 colours( www.korvane-metrics-example.com) it is currently black and white with a small amount of blue/green but I am open to suggestion/interpretations for a consulting company.

Card: I dont mind if it has rounded edges or straight, I was thinking about using a letterpress card if possible

Detail: the detail on the card will include; Name, Title, Mobile, Personal Email, Business Email,Web,Business Address

Once again thanks for submissions

Industry/Entity Type

Business

```html
<!DOCTYPE html>
<html lang="en">
<head>
<meta charset="utf-8">
<title>Korvane Metrics — Business Card</title>
<link rel="stylesheet" href="https://fonts.googleapis.com/css2?family=Montserrat:wght@400;500;600&family=Fira+Sans:wght@300;400&display=swap">
<style>
  :root {
    --backdrop: #e4e4e2;
    --card-white: #ffffff;
    --card-black: #1d1c1c;
    --ink-black: #141414;
    --ink-white: #f4f4f4;
    --ink-muted: #d9d9d9;
    --rule: #bdbdbd;
  }
  * { margin: 0; padding: 0; box-sizing: border-box; }
  html, body {
    width: 1200px;
    height: 873px;
    overflow: hidden;
    background: var(--backdrop);
  }
  .canvas {
    width: 1200px;
    height: 873px;
    display: flex;
    align-items: center;
    justify-content: center;
    gap: 48px;
  }
  .card {
    width: 520px;
    height: 298px;
    position: relative;
    box-shadow: 0 2px 10px rgba(0,0,0,0.12);
  }

  /* Brand side */
  .card--front {
    background: var(--card-white);
    display: flex;
    flex-direction: column;
    align-items: center;
    justify-content: center;
  }
  .brand-name {
    font-family: "Montserrat", sans-serif;
    font-weight: 500;
    font-size: 30px;
    letter-spacing: 0.14em;
    color: var(--ink-black);
    padding-left: 0.14em;
  }
  .brand-tagline {
    margin-top: 12px;
    font-family: "Montserrat", sans-serif;
    font-weight: 400;
    font-size: 8px;
    letter-spacing: 0.32em;
    color: var(--ink-black);
    text-transform: uppercase;
    padding-left: 0.32em;
  }

  /* Contact side */
  .card--back {
    background: var(--card-black);
  }
  .card-frame {
    position: absolute;
    inset: 15px;
    border: 1px solid var(--rule);
  }
  .identity {
    position: absolute;
    top: 60px;
    right: 34px;
    display: flex;
    flex-direction: column;
    align-items: flex-end;
  }
  .person-name {
    font-family: "Montserrat", sans-serif;
    font-weight: 600;
    font-size: 27px;
    letter-spacing: 0.1em;
    color: var(--ink-white);
    line-height: 1;
  }
  .person-title {
    margin-top: 8px;
    background: var(--ink-white);
    color: var(--ink-black);
    font-family: "Montserrat", sans-serif;
    font-weight: 500;
    font-size: 12px;
    letter-spacing: 0.62em;
    padding: 4px 4px 4px 14px;
    line-height: 1;
  }
  .contact-list {
    position: absolute;
    left: 36px;
    bottom: 48px;
    list-style: none;
    font-family: "Fira Sans", sans-serif;
    font-weight: 300;
    font-size: 13px;
    line-height: 1.5;
    letter-spacing: 0.04em;
    color: var(--ink-muted);
  }
</style>
</head>
<body>
  <main class="canvas">
    <section class="card card--back" aria-label="Business card, contact side">
      <div class="card-frame"></div>
      <div class="identity">
        <h1 class="person-name">MARCUS VELL</h1>
        <p class="person-title">FOUNDER &amp; CEO</p>
      </div>
      <ul class="contact-list">
        <li>Telephone: (000) (5550142)</li>
        <li>Mobile: (321) (5550198)</li>
        <li>Email: info@korvane-metrics-example.com</li>
        <li>Website: www.korvane-metrics-example.com</li>
      </ul>
    </section>

    <section class="card card--front" aria-label="Business card, brand side">
      <h2 class="brand-name">KORVANE METRICS</h2>
      <p class="brand-tagline">Assess, Adjust, Advance</p>
    </section>
  </main>
</body>
</html>
```